Tolvane Air and Electrical Website

Simple and easy to use website for a Electrical and Air Conditioning contracting business.Use stock photosOnline contact portallogo still to be supplied

Target Market(s)

Mums and Dads who want a local contractor

Coding

Coded - Design and coding required

Number of Pages Required

2 page

Font styles to use
Sans Serif

Colors
f04a50
3276b5
33a6d7

Requirements
Must have
• Simple and easy to use
• Ph number
• 4 web address; linked to page
• 0417385926
• tolvane.com.au
• tolvaneelectrical.com.au
• tolvaneairandelectrical.com.au
• tolvaneair.com.au
Nice to have
• Split System Air Con Picture
• Electrical Pictures

```html
<!DOCTYPE html>
<html lang="en">
<head>
<meta charset="utf-8">
<title>Tolvane Air and Electrical</title>
<link href="https://fonts.googleapis.com/css2?family=Roboto+Condensed:wght@400;700&display=swap" rel="stylesheet">
<style>
:root{
  --red:#ed1c24;
  --navy:#1b2146;
  --navy-deep:#141a3a;
  --ink:#1c2340;
  --text:#6b6f7e;
  --muted:#8a8fa0;
  --sky:#33a6d7;
  --blue:#3276b5;
  --panel:#eef0f4;
  --white:#ffffff;
}
*{box-sizing:border-box;margin:0;padding:0}
html,body{width:1200px;height:3084px;overflow:hidden}
body{position:relative;background:var(--white);font-family:"Roboto Condensed",Arial,sans-serif;color:var(--ink)}
.abs{position:absolute}
.eyebrow{font-size:11px;letter-spacing:2.6px;text-transform:uppercase;color:var(--text)}
.btn{position:absolute;background:var(--red);color:#fff;font-weight:700;font-size:12px;display:flex;align-items:center;justify-content:center}
.para{font-size:10px;line-height:19px;color:var(--text);font-family:Arial,sans-serif}

/* header */
.brand{left:230px;top:22px;font-size:22px;font-weight:700;color:var(--blue);display:flex;align-items:center;gap:7px;letter-spacing:.5px}
.brand i{width:14px;height:14px;background:var(--red);display:block}
.contact{top:20px;display:flex;gap:10px;align-items:center}
.contact .ring{width:30px;height:30px;border:1px solid #b9dbee;border-radius:50%;display:flex;align-items:center;justify-content:center}
.contact small{display:block;font-size:7px;letter-spacing:1.6px;color:var(--sky)}
.contact span{font-size:9.5px;color:#a4a8b4;font-family:Arial,sans-serif}
.nav{left:230px;top:72px;width:588px;height:48px;background:var(--red);display:flex;align-items:center;padding-left:30px;gap:0}
.nav a{color:#fff;font-size:10.5px;text-decoration:none;margin-right:45px}
.nav a b{font-size:8px}
.quote{left:818px;top:72px;width:152px;height:48px;background:var(--navy);color:#fff;font-weight:700;font-size:11.5px;display:flex;align-items:center;justify-content:center}

/* hero */
.hero{left:0;top:96px;width:1200px;height:525px;background:linear-gradient(90deg,#15161c 0%,#3a3c44 45%,#77797f 75%,#a8a9ac 100%)}
.hero-eyebrow{left:230px;top:280px;color:#fff;font-size:11.5px;letter-spacing:2.4px}
.hero-title{left:228px;top:310px;color:#fff;font-size:66px;font-weight:700;line-height:78px;letter-spacing:-.5px}

/* about */
.about-panel{left:0;top:621px;width:356px;height:520px;background:linear-gradient(180deg,#eef0f4,#ffffff)}
.vertical{left:178px;top:680px;writing-mode:vertical-rl;transform:rotate(180deg);font-size:44px;letter-spacing:14px;color:transparent;-webkit-text-stroke:1px #d4d7df}
.photo{background:linear-gradient(135deg,#5c6a5a,#c9c2b3)}
.circle{left:507px;top:1029px;width:72px;height:72px;border-radius:50%;background:#fff;box-shadow:0 8px 24px rgba(0,0,0,.12);display:flex;align-items:center;justify-content:center}
.h2{font-size:34px;font-weight:700;line-height:42px;color:var(--ink)}
.ticks{left:610px;top:958px;list-style:none}
.ticks li{font-size:11.5px;color:var(--ink);height:25.5px;display:flex;align-items:center;gap:10px}
.ticks li i{width:10px;height:10px;border-radius:50%;background:var(--red);display:flex;align-items:center;justify-content:center}

/* services */
.services{left:0;top:1214px;width:1200px;height:636px;background:var(--panel)}
.card{top:1405px;width:234px;height:368px;background:#fff}
.card .img{height:178px}
.card .badge{position:absolute;left:31px;top:153px;width:45px;height:50px;background:var(--red);display:flex;align-items:center;justify-content:center}
.card h3{position:absolute;left:31px;top:225px;font-size:15px;font-weight:400;color:var(--ink)}
.card p{position:absolute;left:31px;top:252px;width:180px}
.card .more{position:absolute;left:31px;top:328px;width:170px;font-size:9px;letter-spacing:2px;color:var(--red);display:flex;align-items:center;gap:8px}
.card .more::after{content:"";height:1px;flex:1;background:#eceef2}
.card .more b{width:14px;height:1px;background:var(--red);display:block}

/* quality */
.band{left:0;top:1850px;width:1200px;height:252px;background:linear-gradient(90deg,var(--navy) 0%,var(--navy) 55%,#2c3354 80%,#222a4c 100%)}
.promise{left:230px;top:1975px;width:342px;height:487px;background:var(--red);padding:60px 50px 0 62px;color:#fff;font-size:19.5px;line-height:24.4px}

/* testimonials */
.testi{left:0;top:2620px;width:1200px;height:464px;background:linear-gradient(135deg,#1b2146,#232a50 60%,#1b2146)}
.avatar{top:2840px;width:50px;height:50px;border-radius:50%;background:linear-gradient(135deg,#c9a98a,#6d7b6a)}
.avatar.dim{opacity:.35}
.avatar em{position:absolute;right:-3px;bottom:-3px;width:16px;height:16px;border-radius:50%;background:#f05a28}
.who{top:2885px;color:#fff;font-size:11px}
.who small{display:block;font-size:6.5px;letter-spacing:1.4px;margin-top:6px;color:#c6c9d6}
.who.dim{opacity:.35}
.dots{left:936px;top:2734px;display:flex;gap:4px}
.dots i{width:8px;height:8px;border-radius:50%;border:1.5px solid #8a8fa6}
.dots i.on{background:#fff;border-color:#fff}
</style>
</head>
<body>

<!-- header -->
<div class="abs brand"><i></i>TOLVANE</div>
<div class="abs contact" style="left:458px">
  <div class="ring"><svg width="14" height="14" viewBox="0 0 14 14" fill="none" stroke="#5fb4dc"><rect x="2" y="3.5" width="10" height="7"/><path d="M2 3.5l5 4 5-4"/></svg></div>
  <div><small>EMAIL</small><span>support@tolvane-electrical.com.au</span></div>
</div>
<div class="abs contact" style="left:658px">
  <div class="ring"><svg width="14" height="14" viewBox="0 0 14 14" fill="none" stroke="#5fb4dc"><path d="M3 2.5l2.2 0 1 2.6-1.3 1a6 6 0 0 0 3 3l1-1.3 2.6 1v2.2c-5 .6-9.1-3.5-8.5-8.5z"/></svg></div>
  <div><small>PHONE</small><span>0417 385 926</span></div>
</div>
<div class="abs contact" style="left:778px">
  <div class="ring"><svg width="14" height="14" viewBox="0 0 14 14" fill="none" stroke="#5fb4dc"><path d="M7 12.5s-4-3.8-4-7a4 4 0 0 1 8 0c0 3.2-4 7-4 7z"/><circle cx="7" cy="5.5" r="1.4"/></svg></div>
  <div><small>VISIT</small><span>48 Banksia St, Oakleigh Victoria 3166</span></div>
</div>

<!-- hero -->
<div class="abs hero" role="img" aria-label="Electrician's hands wiring a switchboard full of coloured cables"></div>
<nav class="abs nav">
  <a href="#"><strong>Home</strong> <b>▾</b></a>
  <a href="#">Pages <b>▾</b></a>
  <a href="#">Our Services <b>▾</b></a>
  <a href="#">Recent Projects <b>▾</b></a>
  <a href="#">Blog <b>▾</b></a>
  <a href="#">Contact <b>▾</b></a>
</nav>
<div class="abs quote">Get a Free Quote</div>
<div class="abs hero-eyebrow">TOLVANE ELECTRICAL DELIVERS</div>
<h1 class="abs hero-title">Electrical and Split System<br>Installation services</h1>
<div class="btn" style="left:230px;top:474px;width:140px;height:49px">Learn More</div>

<!-- about -->
<div class="abs about-panel"></div>
<div class="abs vertical">TOLVANE</div>
<div class="abs photo" style="left:230px;top:697px;width:316px;height:303px;background:linear-gradient(135deg,#3e6b52,#b9b7ae 60%,#e0ddd6)" role="img" aria-label="Hands testing a circuit board with a multimeter probe"></div>
<div class="abs photo" style="left:178px;top:947px;width:228px;height:181px;background:linear-gradient(135deg,#c9b48e,#8f8472 55%,#e1dccf);box-shadow:0 12px 30px rgba(0,0,0,.15)" role="img" aria-label="Technician servicing a wall-mounted split system air conditioner"></div>
<div class="abs circle"><svg width="30" height="20" viewBox="0 0 30 20" fill="none" stroke="var(--red)" stroke-width="1.2"><rect x="2" y="2" width="26" height="9" rx="1.5"/><path d="M5 8h20M9 14l-1 3M13 14v3M17 14v3M21 14l1 3"/></svg></div>

<div class="abs eyebrow" style="left:610px;top:727px">WELCOME TO TOLVANE</div>
<h2 class="abs h2" style="left:610px;top:743px">Professional Electrical<br>Business since 2014</h2>
<p class="abs para" style="left:610px;top:845px;width:362px">With over 17 years' experience in the Electrical Industry, Tolvane Electrical provides a superior level of knowledge, a broad range of products and a high standard of customer service. To provide our customers with an immediate response within their timeframe, and deliver on-time, every time. Our friendly tradesmen are always professionally attired and treat your home or business with respect - we leave our jobs clean and tidy.</p>
<ul class="abs ticks">
  <li><i><svg width="6" height="6" viewBox="0 0 6 6"><path d="M1 3l1.4 1.4L5 1.6" stroke="#fff" fill="none"/></svg></i>Professional and affordable services</li>
  <li><i><svg width="6" height="6" viewBox="0 0 6 6"><path d="M1 3l1.4 1.4L5 1.6" stroke="#fff" fill="none"/></svg></i>We provide you the highest quality works</li>
  <li><i><svg width="6" height="6" viewBox="0 0 6 6"><path d="M1 3l1.4 1.4L5 1.6" stroke="#fff" fill="none"/></svg></i>Present in the greater Melbourne Area</li>
  <li><i><svg width="6" height="6" viewBox="0 0 6 6"><path d="M1 3l1.4 1.4L5 1.6" stroke="#fff" fill="none"/></svg></i>Great Customer Service</li>
</ul>
<div class="btn" style="left:610px;top:1088px;width:126px;height:49px">Learn More</div>

<!-- services -->
<div class="abs services"></div>
<div class="abs eyebrow" style="left:0;width:1200px;text-align:center;top:1320px">PROFESSIONAL SOLUTIONS</div>
<h2 class="abs h2" style="left:0;width:1200px;text-align:center;top:1336px;font-size:32px">Our Services</h2>

<div class="abs card" style="left:230px">
  <div class="img" style="background:linear-gradient(135deg,#b9bcc1,#e6e7e8 50%,#6c6f78)" role="img" aria-label="Hand holding an air conditioner remote control"></div>
  <div class="badge"><svg width="20" height="20" viewBox="0 0 20 20" fill="none" stroke="#fff" stroke-width="1.3"><path d="M3 9l7-6 7 6M5 8v9h10V8M8.5 17v-5h3v5"/></svg></div>
  <h3>Domestic</h3>
  <p class="para">There are many variations of passages of available but the have alteration in that some form by injected.</p>
  <div class="more">READ MORE <b></b></div>
</div>
<div class="abs card" style="left:483px;box-shadow:0 10px 24px rgba(27,33,70,.08)">
  <div class="img" style="background:linear-gradient(90deg,#f4f4f4,#e2e2e2 55%,#c8a47e 75%,#9a7a5a)" role="img" aria-label="Wall-mounted thermostat and security keypad beside a door"></div>
  <div class="badge"><svg width="22" height="20" viewBox="0 0 22 20" fill="none" stroke="#fff" stroke-width="1.2"><rect x="3" y="3" width="12" height="14"/><rect x="15" y="8" width="5" height="9"/><path d="M6 6h2M10 6h2M6 9h2M10 9h2M6 12h2M10 12h2M8 17v-3h2v3"/></svg></div>
  <h3>Commercial</h3>
  <p class="para">There are many variations of passages of available but the have alteration in that some form by injected.</p>
  <div class="more">READ MORE <b></b></div>
</div>
<div class="abs card" style="left:736px">
  <div class="img" style="background:linear-gradient(135deg,#e8e8e8,#8a93a2 45%,#3d4d72)" role="img" aria-label="Two workers in hard hats installing ceiling ductwork"></div>
  <div class="badge"><svg width="24" height="20" viewBox="0 0 24 20" fill="none" stroke="#fff" stroke-width="1.2"><path d="M2 17V9l5 3V9l5 3V9l5 3V4h4v13z"/><path d="M5 14h2M10 14h2M15 14h2"/></svg></div>
  <h3>Industrial</h3>
  <p class="para">There are many variations of passages of available but the have alteration in that some form by injected.</p>
  <div class="more">READ MORE <b></b></div>
</div>

<!-- quality -->
<div class="abs band" role="img" aria-label="Smiling tradesman in a hard hat on a dark blue tint"></div>
<div class="abs promise">
  <svg width="40" height="44" viewBox="0 0 40 44" fill="none" stroke="#fff" stroke-width="1.5" style="display:block;margin-bottom:16px"><circle cx="20" cy="15" r="8"/><path d="M10 16v-3a10 10 0 0 1 20 0v3M30 16v4h-6"/><path d="M5 42c1-9 7-13 15-13s14 4 15 13z"/><path d="M16 29l4 6 4-6"/></svg>
  We are committed to best practice electrical safety standards and highest quality performance on the job. Our team of qualified and apprentice electricians provide personalised service based on professionalism and integrity. We aim to build long term business relationships and offer information and advice when you need it.
</div>
<div class="abs eyebrow" style="left:608px;top:2140px">WE DELIVER</div>
<h2 class="abs h2" style="left:608px;top:2156px;font-size:32px">Quality</h2>
<p class="abs para" style="left:608px;top:2218px;width:364px">With over 17 years' experience in the Electrical Industry, Tolvane Electrical provides a superior level of knowledge, a broad range of products and a high standard of customer service. To provide our customers with an immediate response within their timeframe, and deliver on-time, every time. Our friendly tradesmen are always professionally attired and treat your home or business with respect - we leave our jobs clean and tidy.</p>
<div class="abs eyebrow" style="left:608px;top:2336px">COST EFFICIENT</div>
<h2 class="abs h2" style="left:608px;top:2352px;font-size:32px">Prices</h2>
<p class="abs para" style="left:608px;top:2415px;width:364px">Price is always important and our standard rates are competitive. Where jobs require an individual approach, we provide a comprehensive quote. Work is completed according to the quote at the agreed price. Registered Contractor Tolvane Electrical is a registered electrical contractor with Power Safety Board, and also a registered CoolTrade contractor to install and decommission split system air conditioning</p>

<!-- testimonials -->
<div class="abs testi" role="img" aria-label="Tradesman's workshop scene on a dark blue tint"></div>
<div class="abs eyebrow" style="left:230px;top:2725px;color:#d5d8e4">OUR TESTIMONAILS</div>
<h2 class="abs h2" style="left:230px;top:2741px;font-size:32px;color:#fff">Happy Customers</h2>
<div class="abs dots"><i class="on"></i><i></i><i></i></div>

<div class="abs avatar" style="left:230px" role="img" aria-label="Customer portrait"><em></em></div>
<div class="abs avatar dim" style="left:325px" role="img" aria-label="Customer portrait"><em></em></div>
<div class="abs avatar dim" style="left:420px" role="img" aria-label="Customer portrait"><em></em></div>
<div class="abs who" style="left:230px;top:2885px">Owen R<small>HOPPERS CROSSING</small></div>
<div class="abs who dim" style="left:325px;top:2885px">Clare<small>PAKENHAM</small></div>
<div class="abs who dim" style="left:420px;top:2885px">Tessa K<small>SANDRINGHAM</small></div>

<p class="abs" style="left:546px;top:2809px;width:424px;color:#fff;font-size:15.5px;line-height:27px">“Excellent service. Declan came and quoted at the agreed time. The team showed up on time an completed on time.&nbsp;&nbsp; Declan and his guys were friendly and professional and I would highly recommend them. I will look to them for any future work”</p>
<div class="abs" style="left:546px;top:2930px;font-size:10px;letter-spacing:2.4px;color:var(--red);font-weight:700">10 MAY, 2019</div>

</body>
</html>
```